Business Card Design

I need a business card for my resume writing business. I have a logo that Im not keen on anymore so I would like the business card to use my photo instead of a logo. I am for mid career and trades resumes and prefer not to do executive resumes so don't need to aim for exectives. I would like it to be colourful. I like bright sky blue and maybe some pink or purple but primarily bright sky blue. I don't like green and Im keen see a fair bit of white on the card. As I have a photo to go it, it will need to go on a white background.

Target Market(s)

mid range careers. Not executives

Industry/Entity Type

Business

Contact Information for Business Card

Wyn Marchetti
Resume Writer
Clear Path CVs
27 The Lanyard
HARWOOD NSW 2465
wyn@clearpathcvs.com.au
0417362958
www.clearpathcvs.com.au

Requirements
Nice to have
• Maybe colours similar to my website - www.clearpathcvs.com.au but not with any black on it.
Should not have
• No green or dark colours

```html
<!DOCTYPE html>
<html lang="en">
<head>
<meta charset="utf-8">
<title>Clear Path CVs – Business Card</title>
<link rel="stylesheet" href="https://fonts.googleapis.com/css2?family=Titillium+Web:wght@300;400;600;700&display=swap">
<style>
  :root {
    --page: #ffffff;
    --card: #ffffff;
    --card-edge: #9a9a9a;
    --ink: #3a3a3c;
    --ink-soft: #6b6b6e;
    --sky: #29a8e0;
    --sky-line: #4fb6e6;
    --mid-blue: #1a75bb;
    --navy: #2b3990;
    --icon-ring: #a9d9f2;
    --photo-light: #e7eef3;
    --photo-mid: #8fa9ba;
    --photo-deep: #4d6f84;
  }
  * { margin: 0; padding: 0; box-sizing: border-box; }
  html, body {
    width: 1200px; height: 767px; overflow: hidden;
    background: var(--page);
    font-family: "Titillium Web", "Helvetica Neue", Arial, sans-serif;
  }
  .card { position: relative; width: 1200px; height: 767px; }
  .card-shape { position: absolute; inset: 0; }

  .brand {
    position: absolute; right: 358px; top: 154px;
    display: flex; align-items: center; gap: 18px;
    font-weight: 700; font-size: 31px; letter-spacing: 1.2px;
    color: var(--ink); line-height: 1;
  }
  .brand-dash { width: 76px; height: 11px; background: var(--sky); }
  .address {
    position: absolute; right: 358px; top: 200px;
    font-size: 28px; font-weight: 400; color: var(--ink-soft);
    letter-spacing: 0.4px; line-height: 1;
  }
  .rule {
    position: absolute; left: 105px; width: 730px; height: 2px;
    background: var(--sky-line);
  }
  .rule-top { top: 288px; }
  .rule-bottom { top: 388px; }

  .title-row {
    position: absolute; left: 106px; right: 354px; top: 312px;
    display: flex; align-items: baseline; justify-content: space-between;
  }
  .role {
    font-size: 20px; font-weight: 700; letter-spacing: 4.5px;
    color: var(--ink);
  }
  .name {
    font-size: 54px; font-weight: 300; letter-spacing: 4.5px;
    color: var(--ink); line-height: 1;
  }

  .contacts { position: absolute; left: 94px; top: 450px; list-style: none; }
  .contact {
    display: flex; align-items: center; gap: 14px;
    height: 56px; margin-bottom: 11px;
    font-size: 29px; color: var(--ink-soft); letter-spacing: 0.3px;
  }
  .contact-icon { width: 56px; height: 56px; flex: none; }
</style>
</head>
<body>
<div class="card">
  <svg class="card-shape" width="1200" height="767" viewBox="0 0 1200 767">
    <defs>
      <clipPath id="card-clip">
        <path d="M141 33 H1143 V615 A105 105 0 0 1 1038 720 H36 V138 A105 105 0 0 1 141 33 Z"/>
      </clipPath>
      <linearGradient id="portrait-tone" x1="0" y1="0" x2="1" y2="0">
        <stop offset="0" stop-color="var(--photo-light)" stop-opacity="0"/>
        <stop offset="0.35" stop-color="var(--photo-light)"/>
        <stop offset="0.7" stop-color="var(--photo-mid)"/>
        <stop offset="1" stop-color="var(--photo-deep)"/>
      </linearGradient>
    </defs>
    <path d="M141 33 H1143 V615 A105 105 0 0 1 1038 720 H36 V138 A105 105 0 0 1 141 33 Z"
          fill="var(--card)" stroke="var(--card-edge)" stroke-width="1.5"/>
    <g clip-path="url(#card-clip)">
      <rect x="700" y="104" width="443" height="586" fill="url(#portrait-tone)"
            role="img" aria-label="Portrait photo of Wyn Marchetti, resume writer, in a light jacket"/>
      <rect x="36" y="690" width="380" height="30" fill="var(--navy)"/>
      <rect x="416" y="690" width="395" height="30" fill="var(--mid-blue)"/>
      <rect x="811" y="690" width="332" height="30" fill="var(--sky)"/>
    </g>
  </svg>

  <div class="brand"><span class="brand-dash"></span><span class="brand-name">CLEAR PATH CVS</span></div>
  <div class="address">27 Lanyard HARWOOD NSW, 2465</div>

  <div class="rule rule-top"></div>
  <div class="title-row">
    <span class="role">RESUME WRITER</span>
    <span class="name">WYN MARCHETTI</span>
  </div>
  <div class="rule rule-bottom"></div>

  <ul class="contacts">
    <li class="contact">
      <svg class="contact-icon" viewBox="0 0 56 56" aria-hidden="true">
        <circle cx="28" cy="28" r="26" fill="var(--icon-ring)"/>
        <circle cx="28" cy="28" r="21" fill="var(--sky)"/>
        <path d="M21 17 l5 0 l2 7 l-3 3 q3 6 8 8 l3-3 l7 2 l0 5 q-1 3-5 3 q-11-1-18-12 q-3-6-2-10 q1-3 3-3z" fill="#fff"/>
      </svg>
      <span>0417 362 958</span>
    </li>
    <li class="contact">
      <svg class="contact-icon" viewBox="0 0 56 56" aria-hidden="true">
        <circle cx="28" cy="28" r="26" fill="var(--icon-ring)"/>
        <circle cx="28" cy="28" r="21" fill="var(--sky)"/>
        <rect x="15" y="19" width="26" height="18" fill="none" stroke="#fff" stroke-width="2.5"/>
        <path d="M15 19 L28 30 L41 19 M15 37 L24 27 M41 37 L32 27" fill="none" stroke="#fff" stroke-width="2.2"/>
      </svg>
      <span>wyn@clearpathcvs.com.au</span>
    </li>
    <li class="contact">
      <svg class="contact-icon" viewBox="0 0 56 56" aria-hidden="true">
        <circle cx="28" cy="28" r="26" fill="var(--icon-ring)"/>
        <circle cx="28" cy="28" r="21" fill="var(--sky)"/>
        <path d="M22 14 L22 38 L27 33 L31 42 L35 40 L31 31 L38 31 Z" fill="#fff"/>
      </svg>
      <span>www.clearpathcvs.com.au</span>
    </li>
  </ul>
</div>
</body>
</html>
```